依頼詳細
チラシを持参してもらったお客様限定のお試し価格の案内チラシを作成したいと思います。
普段のお客様ですと、お店の高級感から敷居が高いように感じられがちですが、
今回は、少しライトな層を狙えるようなイメージを持っています。
記載項目
◆焼肉バー ミヨコ

・ぐるめ帳ページ
https://gurumecho.example/aichi/B4812/B481207/58194630/

・Picstream
https://www.picstream.example/miyoko_yakiniku_bar/
サイズ
A5
ページ数
片面
希望イメージ
シンプル 複雑
単色 カラフル
暗い 明るい
日常 高級
遊び心 厳粛
未来的 伝統的
女性的 男性的
希望する色
黄・オレンジ系、無彩色系
納品ファイル
• 高解像度JPG (.jpg)
• イラストレーター形式 (.ai)
補足説明

```html
<!DOCTYPE html>
<html lang="ja">
<head>
<meta charset="utf-8">
<title>焼肉BAR MIYOKO お試しコース</title>
<link href="https://fonts.googleapis.com/css2?family=Noto+Sans+JP:wght@400;700;900&family=Shippori+Mincho:wght@600;800&family=Noto+Serif+JP:wght@700;900&display=swap" rel="stylesheet">
<style>
  :root {
    --ink: #1b1a19;
    --paper: #f6f1ea;
    --orange: #e8741f;
    --orange-deep: #d2581a;
    --red: #d8281e;
    --white: #ffffff;
    --muted: #4a433d;
    --meat: #b8464a;
    --meat-deep: #7a2a2c;
    --straw: #a88a4a;
    --table: #26211f;
  }
  * { margin: 0; padding: 0; box-sizing: border-box; }
  html, body { width: 847px; height: 1200px; overflow: hidden; background: var(--white); }
  .flyer {
    position: relative; width: 847px; height: 1200px; overflow: hidden;
    background: var(--paper);
    font-family: "Noto Sans JP", sans-serif; color: var(--ink);
  }
  .hero-photo {
    position: absolute; left: 0; top: 0; width: 847px; height: 650px;
    background:
      radial-gradient(ellipse 240px 170px at 440px 250px, rgba(200,80,82,0.95), rgba(200,80,82,0) 100%),
      radial-gradient(ellipse 170px 120px at 90px 420px, rgba(176,64,66,0.85), rgba(176,64,66,0) 100%),
      radial-gradient(ellipse 160px 120px at 770px 230px, rgba(184,72,74,0.8), rgba(184,72,74,0) 100%),
      radial-gradient(ellipse 220px 110px at 420px 560px, rgba(168,60,60,0.85), rgba(168,60,60,0) 100%),
      radial-gradient(ellipse 170px 120px at 760px 520px, rgba(214,170,110,0.7), rgba(214,170,110,0) 100%),
      radial-gradient(ellipse 300px 200px at 440px 300px, rgba(168,138,74,0.45), rgba(168,138,74,0) 100%),
      linear-gradient(180deg, #2c2624 0%, var(--table) 60%, #3a3230 100%);
  }
  .hero-fade {
    position: absolute; left: 0; top: 590px; width: 847px; height: 60px;
    background: linear-gradient(180deg, rgba(246,241,234,0), var(--paper));
  }
  .brand-mark {
    position: absolute; left: 0; top: 0; width: 170px; height: 170px;
    background: var(--ink); display: flex; align-items: flex-end; justify-content: center;
    padding-bottom: 36px;
  }
  .brand-mark span {
    color: var(--white); font-family: "Noto Serif JP", serif; font-weight: 700;
    font-size: 22px; letter-spacing: 4px;
  }
  .tagline {
    position: absolute; top: 662px; left: 0; width: 100%; text-align: center;
    font-family: "Shippori Mincho", serif; font-weight: 600; font-size: 24px; color: var(--orange-deep);
    letter-spacing: 1px;
  }
  .title {
    position: absolute; top: 700px; left: 0; width: 100%; text-align: center;
    font-family: "Noto Serif JP", serif; font-weight: 900; line-height: 1.3; white-space: nowrap;
  }
  .title .bar-label { font-size: 50px; color: var(--orange); margin-right: 22px; letter-spacing: 1px; }
  .title .name { font-size: 74px; letter-spacing: 14px; color: var(--ink); }
  .title-rule {
    position: absolute; top: 812px; left: 60px; width: 727px; height: 3px; background: var(--orange);
  }
  .trial-card {
    position: absolute; left: 36px; top: 838px; width: 290px; height: 170px;
    background: var(--white); border: 3px solid var(--orange); border-radius: 6px;
  }
  .trial-card .label {
    position: absolute; top: 10px; left: 50%; transform: translateX(-50%);
    background: var(--orange); color: var(--white); font-weight: 700; font-size: 22px; line-height: 1.4;
    padding: 1px 20px; border-radius: 16px; white-space: nowrap;
  }
  .trial-card .price {
    position: absolute; top: 52px; left: 18px;
    font-weight: 900; font-size: 88px; line-height: 1;
    color: var(--red); letter-spacing: -2px; white-space: nowrap;
  }
  .trial-card .yen { font-size: 38px; letter-spacing: 0; }
  .trial-card .exact {
    position: absolute; top: 56px; right: 14px; font-size: 12px; font-weight: 700; color: var(--red);
  }
  .trial-card .tax {
    position: absolute; top: 82px; right: 14px; width: 44px; height: 44px; border-radius: 50%;
    background: var(--red); color: var(--white); font-size: 13px; font-weight: 700;
    display: flex; align-items: center; justify-content: center;
  }
  .course-items {
    position: absolute; left: 36px; top: 1020px; width: 300px;
    font-size: 11px; line-height: 1.75; color: var(--muted); white-space: nowrap;
  }
  .limited {
    position: absolute; left: 370px; top: 840px; width: 450px;
    font-weight: 900; font-size: 32px; line-height: 1.5; color: var(--red);
  }
  .limited .big { font-size: 52px; }
  .limited .line { display: block; border-bottom: 3px solid var(--orange); width: fit-content; white-space: nowrap; }
  .notes {
    position: absolute; left: 370px; top: 990px; width: 450px;
    font-size: 14px; line-height: 1.75; color: var(--ink); white-space: nowrap;
  }
  .footer {
    position: absolute; left: 0; bottom: 0; width: 847px; height: 88px; background: var(--ink);
    color: var(--white); display: flex; align-items: center; justify-content: space-between; padding: 0 36px;
  }
  .footer .shop-name { font-size: 20px; font-weight: 700; }
  .footer .shop-name small {
    font-size: 12px; background: var(--white); color: var(--ink); padding: 1px 6px; margin-right: 8px;
    vertical-align: middle;
  }
  .footer .address { font-size: 14px; margin-top: 4px; }
  .footer .tel { font-size: 26px; font-weight: 700; letter-spacing: 1px; line-height: 1.3; }
  .footer .tel small { font-size: 14px; margin-right: 6px; }
  .footer .hours { font-size: 15px; }
</style>
</head>
<body>
<div class="flyer">
  <div class="hero-photo" role="img" aria-label="黒い器や藁の上に盛り付けられた霜降り和牛ステーキ、ロース、牛タン、ホルモンなど焼肉料理の写真"></div>
  <div class="hero-fade"></div>
  <div class="brand-mark"><span>MIYOKO</span></div>

  <p class="tagline">鍋でお得に、ちょっと贅沢なひとときを</p>
  <h1 class="title"><span class="bar-label">焼肉BAR</span><span class="name">MIYOKO</span></h1>
  <div class="title-rule"></div>

  <div class="trial-card">
    <span class="label">お試しコース</span>
    <span class="exact">ポッキリ!</span>
    <p class="price">980<span class="yen">円</span></p>
    <span class="tax">税込</span>
  </div>
  <p class="course-items">厚切り牛タン／黒毛和牛カルビ／ミヨコサラダ／本日の赤身<br>季節のナムル／特製ホルモン／ご飯セット／デザート</p>

  <p class="limited">
    <span class="line">今から<span class="big">30</span>分以内に</span>
    <span class="line">ご来店のお客様限定コース!!</span>
  </p>
  <p class="notes">
    チラシをお持ちのお客様限定の特別コースでございます。<br>
    ご来店の際、お持ち頂きスタッフにご提示ください。<br>
    ※お試しコースはお一人様1回限りとさせて頂きます。
  </p>

  <footer class="footer">
    <div class="shop">
      <p class="shop-name"><small>焼肉バー</small>ミヨコ</p>
      <p class="address">名古屋市中区栄5-8-12 灯りビル3F</p>
    </div>
    <div class="contact">
      <p class="tel"><small>TEL</small>052-000-4719</p>
      <p class="hours">18:00-5:00(L.O. 3:00)</p>
    </div>
  </footer>
</div>
</body>
</html>
```